依頼詳細
表面は、
ロゴ
名前
会社名
本社の住所等で、(電話はいりません)

裏面には、3つの事業の情報をお願いします。
記載項目
添付いたします
希望イメージ
シンプル 複雑
単色 カラフル
暗い 明るい
日常 高級
遊び心 厳粛
未来的 伝統的
女性的 男性的
希望する色
赤系
納品ファイル
補足説明

```html
<!DOCTYPE html>
<html lang="ja">
<head>
<meta charset="utf-8">
<title>名刺 表面</title>
<link rel="stylesheet" href="https://fonts.googleapis.com/css2?family=Noto+Serif+JP:wght@400;500&display=swap">
<style>
  :root {
    --card-red: #c8524e;
    --ink-white: #ffffff;
  }
  html, body {
    margin: 0;
    padding: 0;
    overflow: hidden;
    background: var(--card-red);
  }
  .card {
    position: relative;
    width: 711px;
    height: 1200px;
    background: var(--card-red);
    color: var(--ink-white);
    font-family: "Noto Serif JP", serif;
    overflow: hidden;
  }
  .card p { margin: 0; }
  .logo-mark {
    position: absolute;
    top: 252px;
    left: 0;
    width: 100%;
    text-align: center;
    font-size: 32px;
    letter-spacing: 2px;
  }
  .person {
    position: absolute;
    top: 408px;
    left: 0;
    width: 100%;
    text-align: center;
  }
  .person__title {
    font-size: 34px;
    letter-spacing: 2px;
    line-height: 50px;
  }
  .person__name-jp {
    font-size: 34px;
    letter-spacing: 4px;
    word-spacing: 30px;
    line-height: 46px;
  }
  .person__name-en {
    font-size: 37px;
    letter-spacing: 1px;
    word-spacing: 22px;
    line-height: 50px;
  }
  .company {
    position: absolute;
    top: 775px;
    left: 344px;
    font-size: 24px;
    letter-spacing: 1px;
  }
  .address {
    position: absolute;
    top: 840px;
    left: 240px;
    width: 430px;
    text-align: center;
    font-size: 23px;
    line-height: 36px;
    font-weight: 500;
  }
  .icon {
    position: absolute;
    fill: none;
    stroke: var(--ink-white);
    stroke-width: 3;
  }
  .icon--pin { left: 144px; top: 876px; }
  .icon--mail { left: 140px; top: 990px; }
  .website {
    position: absolute;
    top: 990px;
    left: 284px;
    font-size: 23px;
    font-weight: 500;
  }
</style>
</head>
<body>
  <main class="card">
    <p class="logo-mark">ロゴ</p>

    <section class="person">
      <p class="person__title">マネージャー</p>
      <p class="person__name-jp">●● ●●</p>
      <p class="person__name-en">Sato Kenji</p>
    </section>

    <p class="company">(株) 桜木学院</p>

    <svg class="icon icon--pin" width="44" height="60" viewBox="0 0 44 60" aria-hidden="true">
      <path d="M22 50 C12 36 6 28 6 20 A16 16 0 0 1 38 20 C38 28 32 36 22 50 Z"/>
      <circle cx="22" cy="20" r="6"/>
      <path d="M10 46 C3 48 3 52 10 54 C16 56 28 56 34 54 C41 52 41 48 34 46"/>
    </svg>
    <address class="address" style="font-style: normal;">
      <p>〒104-0053</p>
      <p>東京都中央区晴海2丁目4番18号</p>
      <p>晴海サンライズビルA棟７階</p>
    </address>

    <svg class="icon icon--mail" width="64" height="46" viewBox="0 0 64 46" aria-hidden="true">
      <rect x="3" y="3" width="58" height="40" rx="2"/>
      <path d="M3 3 L32 27 L61 3"/>
      <path d="M3 43 L24 21 M61 43 L40 21"/>
    </svg>
    <p class="website">http://sakuragigakuin.com/</p>
  </main>
</body>
</html>
```